Need a high-impact website built for used car dealership

I am seeking a high impact website built on Pagecrate for my used car dealership.

The name of the dealership is Roadline Motor Depot, Inc. A copy of our logo is attached. Our company colors are blue and orange and should be incorporated into the website.

The overall look and feel of the website should be clean, easy to navigate, classy yet contemporary. Customers should be able to navigate the site quickly without it being cumbersome.The site should look custom built and NOT like a generic template.

Here are some details that must be incorporated into the final product:
** The site should be highly optimized for white hat SEO (headlines, content, page structure; keyword use, title tags, meta descriptions, clean index, fast page loads, etc)
** Site must be fully mobile responsive
** Site should be setup for Trackwise Metrics and Chatterbox Beacon tracking
** Site must include live chat functionality; if no one is available to respond to the live chat the system should send an email with the consumers information.
** Include a "like" button that allows customers to like/follow our Chatterbox page from the website
** Include exit prompt/popup to collect email address and phone number
** Include a finance app (example: https://www.harlowmotorsdemo.com/FinancePreQualForm)
** Include a reviews function similiar to the one on tallbrooks page: https://www.tallbrook-demo.com/write-review-select-rating/
If customer selects 1, 2, or 3 star rating they post a review that is sent to us via email; If customer selects 4 or 5 star rating it posts a Searchly or Tattlo review which becomes visible on the site
** Include ability to email or text message a link to a specific vehicle
** Include ability for customer to share a vehicle on Chatterbox
** Include ability for user to mark specific vehicles "favorites" so they can easily view them again
** Include ability to filter vehicles by year, make, model, mileage, color and drivetrain or any combination of those when searching inventory
** include paygatex.example credit card payments.
** Customer must be able to call our dealership on a mobile device by clicking on the phone number on the main page
**Customer must be able to click on our address on the main page and have it link to their native maps app on their mobile device
** Vehicle inventory will import from our LotListings.example account. The listing data will be provided in a CSV or TXT file, which will include links to the photographs of the vehicles.
** Include logos of all the major car manufacturers on the home page: Velmar, Orvo, KTZ, Pellam, Montravel, Darnshire, Wexmoore, Brant, Klay, PVT, Zerta, Tovarin, Solvane, Falmont, Trok, Oze, Moor Trekker, Quoran, Ashbury, Pelto, Halvorsen Stahl, Pipo, Taveno, Wendrick, Elk, Vance-Hartley, Tiro, Lumet, Kovena, Voltan, Marekko, Drevstadt, and Grenn.

Attached is one example I like. I’d like to see a design like this as well as your own creative work.

• See above
• Site must have a clean, custom look that does not appear to be a cookie-cutter website

```html
<!DOCTYPE html>
<html lang="en">
<head>
<meta charset="utf-8">
<title>Roadline Motor Depot – Used Cars</title>
<link href="https://fonts.googleapis.com/css2?family=Montserrat:wght@400;500;600;700&family=Oswald:wght@500&family=Open+Sans:wght@400;600&display=swap" rel="stylesheet">
<style>
:root{
  --blue:#1a62b8;
  --blue-dark:#0c4a9e;
  --blue-light:#1f86d3;
  --orange:#ff6612;
  --black:#0b0b0b;
  --footer:#1e1e1e;
  --gray-bg:#f1f1f1;
  --line:#dcdcdc;
  --text:#333;
  --muted:#666;
  --white:#fff;
}
*{box-sizing:border-box;margin:0;padding:0}
html,body{width:1200px;height:4706px;overflow:hidden}
body{font-family:"Open Sans",sans-serif;color:var(--text);background:var(--white);position:relative}
.abs{position:absolute}
svg{display:block}
h2.section-title{position:absolute;left:0;width:1200px;text-align:center;font-family:"Montserrat",sans-serif;font-weight:600;font-size:38px;color:#222;letter-spacing:.5px}
h2.section-title span{color:var(--blue)}

.site-header{position:absolute;left:0;top:0;width:1200px;height:128px;background:var(--black)}
.brand{position:absolute;left:170px;top:34px;font-family:"Montserrat",sans-serif;font-weight:700;color:var(--white);line-height:1}
.brand .b1{font-size:32px;letter-spacing:-.5px;display:block}
.brand .b2{font-size:13px;letter-spacing:5.5px;display:block;margin-top:4px}
.topbar{position:absolute;top:28px;right:173px;display:flex;align-items:center;gap:22px;font-family:"Montserrat",sans-serif;font-size:13px;color:var(--white)}
.topbar .sales{font-size:16px;font-weight:600;display:flex;align-items:center;gap:7px}
.topbar .sales b{color:var(--orange);font-weight:600}
.topbar .tl{display:flex;align-items:center;gap:5px}
.topbar .tl.login{color:var(--orange)}
.main-nav{position:absolute;top:79px;left:539px;display:flex;font-family:"Montserrat",sans-serif;font-size:14px;font-weight:500;color:var(--white)}
.main-nav a{color:inherit;text-decoration:none;margin-right:41px}
.main-nav a.active{color:var(--blue-light)}
.nav-search{position:absolute;left:1010px;top:81px}

.hero{position:absolute;left:0;top:128px;width:1200px;height:552px;background:linear-gradient(180deg,#b89a73 0%,#d8b483 22%,#8c7d6b 45%,#5e5349 70%,#4a4038 100%)}
.hero h1{position:absolute;top:128px;left:0;width:1200px;text-align:center;font-family:"Montserrat",sans-serif;font-weight:600;font-size:46px;color:var(--white);letter-spacing:.5px}
.search-box{position:absolute;left:161px;top:215px;width:878px;height:130px;background:rgba(255,255,255,.35);border-radius:3px}
.field{position:absolute;height:46px;background:var(--white);border-radius:2px;font-family:"Montserrat",sans-serif;font-size:14px;color:#444;padding:14px 12px}
.field::after{content:"";position:absolute;right:12px;top:20px;border-left:4px solid transparent;border-right:4px solid transparent;border-top:5px solid #555}
.btn-search{position:absolute;left:723px;top:73px;width:143px;height:46px;background:var(--orange);color:var(--white);font-family:"Montserrat",sans-serif;font-size:14px;font-weight:600;display:flex;align-items:center;justify-content:center;gap:6px;border-radius:2px}
.hero-arrow{position:absolute;top:262px}

.used-cars{position:absolute;left:0;top:680px;width:1200px;height:1100px;background:var(--gray-bg)}
.car-card{position:absolute;width:267px;height:413px;background:var(--white);border:1px solid #e2e2e2;text-align:center;font-family:"Montserrat",sans-serif}
.car-card.featured{border:2px solid var(--blue)}
.car-photo{height:190px;width:100%}
.call-bar{height:40px;background:#e4e4e4;display:flex;align-items:center;justify-content:center;gap:8px;font-size:17px;font-weight:500;color:#333}
.featured .call-bar{background:var(--blue);color:var(--white)}
.price{margin-top:13px;font-size:19px;font-weight:600;color:var(--blue)}
.car-name{margin-top:8px;font-size:13px;line-height:19px;color:#333;height:38px}
.drive{margin-top:13px;font-size:13px;color:var(--blue)}
.card-meta{position:absolute;left:18px;right:18px;bottom:0;height:58px;border-top:1px solid #e5e5e5;display:flex;align-items:center;justify-content:center;gap:16px;font-size:12px;color:#444}
.card-meta span{display:flex;align-items:center;gap:5px}
.btn{position:absolute;background:var(--orange);color:var(--white);font-family:"Montserrat",sans-serif;font-weight:600;font-size:14px;display:flex;align-items:center;justify-content:center;border-radius:2px}

.side-tab{position:absolute;left:1143px;width:57px;height:48px;border-radius:24px 0 0 24px;display:flex;align-items:center;padding-left:12px}
.side-tab i{width:28px;height:28px;border-radius:50%;background:rgba(255,255,255,.95);display:flex;align-items:center;justify-content:center}

.reviews{position:absolute;left:0;top:1780px;width:1200px;height:430px;background:linear-gradient(90deg,var(--blue-dark),var(--blue-light))}
.reviews h2{position:absolute;top:66px;left:0;width:1200px;text-align:center;font-family:"Montserrat",sans-serif;font-weight:600;font-size:30px;color:var(--white)}
.avatar{position:absolute;width:120px;height:120px;border-radius:50%;border:4px solid rgba(255,255,255,.85);background:linear-gradient(160deg,#9b8a7c,#5d4d43)}
.review{position:absolute;width:270px;font-family:"Montserrat",sans-serif;color:var(--white)}
.review .stars{font-size:13px;letter-spacing:2px}
.review p{margin-top:12px;font-family:"Open Sans",sans-serif;font-size:12.5px;line-height:24px;color:#e9f1fb}
.review .who{margin-top:12px;font-size:17px;font-weight:600}

.finance-media{position:absolute;left:172px;top:2297px;width:442px;height:351px;background:#2f2f2f}
.finance-title{position:absolute;left:656px;top:2316px;font-family:"Montserrat",sans-serif;font-weight:600;font-size:30px;color:#222}
.finance-title span{color:var(--blue)}
.finance-text{position:absolute;left:658px;top:2367px;width:365px;font-size:10.6px;line-height:20px;color:#555;text-align:justify}

.promo{position:absolute;left:0;top:2724px;width:1200px;height:152px;background:var(--orange)}
.promo p{position:absolute;left:245px;top:48px;font-family:"Montserrat",sans-serif;font-weight:600;font-size:22px;line-height:29px;color:var(--white)}
.promo .btn-dark{position:absolute;left:851px;top:50px;width:177px;height:49px;background:#1b1b1b;border:1px solid #444;border-radius:3px;color:var(--white);font-family:"Montserrat",sans-serif;font-weight:600;font-size:13px;display:flex;align-items:center;justify-content:center}

.tiles{position:absolute;left:0;top:2876px;width:1200px;height:434px;background:var(--gray-bg)}
.tile{position:absolute;top:75px;width:414px;height:276px}
.tile span{position:absolute;left:0;bottom:26px;width:100%;text-align:center;font-family:"Montserrat",sans-serif;font-weight:600;font-size:19px;color:var(--white)}

.clients-title{font-family:"Oswald",sans-serif !important;font-weight:500 !important;font-size:36px !important}
.client{position:absolute;width:159px;height:91px;background:var(--white);box-shadow:0 1px 6px rgba(0,0,0,.12);display:flex;align-items:center;justify-content:center;gap:8px;font-family:"Montserrat",sans-serif;font-weight:700;font-size:16px;color:#2a2a2a;letter-spacing:.5px}
.client i{width:14px;height:14px;border-radius:50%;background:#2a2a2a}
.dots{position:absolute;top:3714px;left:556px;display:flex;gap:10px}
.dots b{width:9px;height:9px;border-radius:50%;background:#bbb}
.dots b.on{background:#222}

.pop{position:absolute;top:3908px;width:203px;height:239px}
.pop span{position:absolute;left:0;bottom:38px;width:100%;text-align:center;font-family:"Montserrat",sans-serif;font-weight:600;font-size:14px;color:var(--white)}

.site-footer{position:absolute;left:0;top:4240px;width:1200px;height:466px}
.foot-brand{position:absolute;left:0;top:115px;width:1200px;text-align:center;font-family:"Montserrat",sans-serif;font-weight:700;color:var(--white);line-height:1}
.foot-brand .b1{font-size:40px;display:block}
.foot-brand .b2{font-size:16px;letter-spacing:7px;display:block;margin-top:6px}
.pay{position:absolute;top:140px;width:24px;height:15px;border-radius:2px}
.social{position:absolute;left:882px;top:136px;display:flex;align-items:center;gap:12px;font-family:"Montserrat",sans-serif;font-size:13px;color:var(--white)}
.social i{width:28px;height:28px;background:#2d86e0;border-radius:2px}
.contact-col{position:absolute;top:230px;width:296px;text-align:center;font-family:"Montserrat",sans-serif;color:var(--white)}
.contact-col h3{margin-top:14px;font-size:19px;font-weight:500;letter-spacing:.5px}
.contact-col p{margin-top:12px;font-size:11px;line-height:18px;color:#ddd}
.contact-col a{color:#3b8fe6}
.col-divider{position:absolute;top:230px;width:1px;height:110px;background:#555}
.copy{position:absolute;top:402px;left:172px;font-size:11px;color:#ccc}
.foot-links{position:absolute;top:402px;left:657px;display:flex;gap:22px;font-size:11px;color:#ccc}
.mini{position:absolute;top:404px;left:1097px;font-size:10px;color:#999}
</style>
</head>
<body>

<header class="site-header">
  <div class="brand"><span class="b1">Roadline</span><span class="b2">MOTOR DEPOT</span></div>
  <div class="topbar">
    <div class="sales">
      <svg width="15" height="15" viewBox="0 0 24 24" fill="none" stroke="#fff" stroke-width="2"><path d="M22 16.9v3a2 2 0 0 1-2.2 2 19.8 19.8 0 0 1-8.6-3.1 19.5 19.5 0 0 1-6-6A19.8 19.8 0 0 1 2.1 4.2 2 2 0 0 1 4.1 2h3a2 2 0 0 1 2 1.7c.1 1 .4 1.9.7 2.8a2 2 0 0 1-.5 2.1L8 9.9a16 16 0 0 0 6 6l1.3-1.3a2 2 0 0 1 2.1-.4c.9.3 1.8.6 2.8.7a2 2 0 0 1 1.7 2z"/></svg>
      Sales: <b>(555) 014-2277</b>
    </div>
    <div class="tl"><svg width="13" height="13" viewBox="0 0 24 24" fill="none" stroke="#ff6612" stroke-width="2.4"><path d="M20.8 4.6a5.5 5.5 0 0 0-7.8 0L12 5.7l-1-1.1a5.5 5.5 0 0 0-7.8 7.8L12 21.2l8.8-8.8a5.5 5.5 0 0 0 0-7.8z"/></svg>Favorites</div>
    <div class="tl login"><svg width="13" height="13" viewBox="0 0 24 24" fill="none" stroke="#ff6612" stroke-width="2.4"><circle cx="12" cy="8" r="4"/><path d="M4 21c0-4 4-6 8-6s8 2 8 6"/></svg>Login</div>
  </div>
  <nav class="main-nav">
    <a class="active">Home</a><a>About Us</a><a>Inventory</a><a>Finance</a><a>Contact</a>
  </nav>
  <svg class="nav-search" width="15" height="15" viewBox="0 0 24 24" fill="none" stroke="#fff" stroke-width="3"><circle cx="10" cy="10" r="7"/><path d="M15 15l6 6"/></svg>
</header>

<section class="hero" role="img" aria-label="Sunset photo of a couple seated on a rocky riverbank beside a silver SUV">
  <h1>WELCOME TO ROADLINE MOTOR DEPOT</h1>
  <svg class="hero-arrow" style="left:22px" width="34" height="64" viewBox="0 0 34 64" fill="none" stroke="#fff" stroke-width="2"><path d="M32 2L2 32l30 30"/></svg>
  <svg class="hero-arrow" style="left:1144px" width="34" height="64" viewBox="0 0 34 64" fill="none" stroke="#fff" stroke-width="2"><path d="M2 2l30 30L2 62"/></svg>
  <div class="search-box">
    <div class="field" style="left:12px;top:17px;width:276px">Year</div>
    <div class="field" style="left:299px;top:17px;width:276px">Make</div>
    <div class="field" style="left:586px;top:17px;width:280px">Model</div>
    <div class="field" style="left:12px;top:73px;width:276px">Mileage</div>
    <div class="field" style="left:299px;top:73px;width:203px">Color</div>
    <div class="field" style="left:511px;top:73px;width:203px">Drivetrain</div>
    <div class="btn-search"><svg width="13" height="13" viewBox="0 0 24 24" fill="none" stroke="#fff" stroke-width="3.5"><circle cx="10" cy="10" r="7"/><path d="M15 15l6 6"/></svg>SEARCH</div>
  </div>
  <svg class="abs" style="left:0;top:512px" width="1200" height="41" viewBox="0 0 1200 41" preserveAspectRatio="none"><path d="M0 41C300 -12 900 -12 1200 41z" fill="#f1f1f1"/></svg>
</section>

<section class="used-cars">
  <h2 class="section-title" style="top:20px">USED <span>CARS</span></h2>

  <div class="car-card" style="left:172px;top:109px">
    <div class="car-photo" role="img" aria-label="Silver compact sedan photo" style="background:linear-gradient(160deg,#e6e8ea,#b8bcc0 55%,#8d9196)"></div>
    <div class="call-bar"><svg width="15" height="15" viewBox="0 0 24 24" fill="currentColor"><path d="M6.6 10.8a15.1 15.1 0 0 0 6.6 6.6l2.2-2.2a1 1 0 0 1 1-.3c1.1.4 2.3.6 3.6.6a1 1 0 0 1 1 1V20a1 1 0 0 1-1 1A17 17 0 0 1 3 4a1 1 0 0 1 1-1h3.5a1 1 0 0 1 1 1c0 1.3.2 2.5.6 3.6a1 1 0 0 1-.3 1z"/></svg>Call Us: 555 010 2545</div>
    <div class="price">$14 490</div>
    <div class="car-name">2006 Klay Tessa KX2 GT<br>4dr Sedan Tessa</div>
    <div class="drive">Drive Train :FWD</div>
    <div class="card-meta"><span>⋖ Share</span><span>♡ Like</span><span>▣ 2006</span></div>
  </div>

  <div class="car-card featured" style="left:466px;top:109px">
    <div class="car-photo" role="img" aria-label="Black sedan photo" style="background:linear-gradient(160deg,#7a8088,#2c2f33 55%,#1a1b1d)"></div>
    <div class="call-bar"><svg width="15" height="15" viewBox="0 0 24 24" fill="currentColor"><path d="M6.6 10.8a15.1 15.1 0 0 0 6.6 6.6l2.2-2.2a1 1 0 0 1 1-.3c1.1.4 2.3.6 3.6.6a1 1 0 0 1 1 1V20a1 1 0 0 1-1 1A17 17 0 0 1 3 4a1 1 0 0 1 1-1h3.5a1 1 0 0 1 1 1c0 1.3.2 2.5.6 3.6a1 1 0 0 1-.3 1z"/></svg>Call Us: 555 010 2545</div>
    <div class="price">$14 490</div>
    <div class="car-name">2012 Grenn Ostra M4<br>4dr Sedan Ostra</div>
    <div class="drive">Drive Train :FWD</div>
    <div class="card-meta"><span>⋖ Share</span><span>♡ Like</span><span>▣ 2012</span></div>
  </div>

  <div class="car-card" style="left:758px;top:109px">
    <div class="car-photo" role="img" aria-label="Silver pickup truck photo" style="background:linear-gradient(160deg,#c8ccd0,#9ea3a8 55%,#6f7478)"></div>
    <div class="call-bar"><svg width="15" height="15" viewBox="0 0 24 24" fill="currentColor"><path d="M6.6 10.8a15.1 15.1 0 0 0 6.6 6.6l2.2-2.2a1 1 0 0 1 1-.3c1.1.4 2.3.6 3.6.6a1 1 0 0 1 1 1V20a1 1 0 0 1-1 1A17 17 0 0 1 3 4a1 1 0 0 1 1-1h3.5a1 1 0 0 1 1 1c0 1.3.2 2.5.6 3.6a1 1 0 0 1-.3 1z"/></svg>Call Us: 555 010 2545</div>
    <div class="price">$14 490</div>
    <div class="car-name">2013 Darnshire Haulmark<br>2200 RT 4×4 4dr Crew Cab 5.8 ft.</div>
    <div class="drive">Drive Train :FWD</div>
    <div class="card-meta"><span>⋖ Share</span><span>♡ Like</span><span>▣ 2013</span></div>
  </div>

  <div class="car-card" style="left:172px;top:551px">
    <div class="car-photo" role="img" aria-label="Silver pickup truck in a dealer lot" style="background:linear-gradient(160deg,#bfc6cc,#939aa1 55%,#6b7075)"></div>
    <div class="call-bar"><svg width="15" height="15" viewBox="0 0 24 24" fill="currentColor"><path d="M6.6 10.8a15.1 15.1 0 0 0 6.6 6.6l2.2-2.2a1 1 0 0 1 1-.3c1.1.4 2.3.6 3.6.6a1 1 0 0 1 1 1V20a1 1 0 0 1-1 1A17 17 0 0 1 3 4a1 1 0 0 1 1-1h3.5a1 1 0 0 1 1 1c0 1.3.2 2.5.6 3.6a1 1 0 0 1-.3 1z"/></svg>Call Us: 555 010 2545</div>
    <div class="price">$14 490</div>
    <div class="car-name">2009 Darnshire Haulmark 2200<br>Work Truck 4×4 4dr Crew</div>
    <div class="drive">Drive Train :FWD</div>
    <div class="card-meta"><span>⋖ Share</span><span>♡ Like</span><span>▣ 2009</span></div>
  </div>

  <div class="car-card" style="left:466px;top:551px">
    <div class="car-photo" role="img" aria-label="White wagon in a dealer lot" style="background:linear-gradient(160deg,#d9dcdf,#b3b7bb 55%,#7f8388)"></div>
    <div class="call-bar"><svg width="15" height="15" viewBox="0 0 24 24" fill="currentColor"><path d="M6.6 10.8a15.1 15.1 0 0 0 6.6 6.6l2.2-2.2a1 1 0 0 1 1-.3c1.1.4 2.3.6 3.6.6a1 1 0 0 1 1 1V20a1 1 0 0 1-1 1A17 17 0 0 1 3 4a1 1 0 0 1 1-1h3.5a1 1 0 0 1 1 1c0 1.3.2 2.5.6 3.6a1 1 0 0 1-.3 1z"/></svg>Call Us: 555 010 2545</div>
    <div class="price">$14 490</div>
    <div class="car-name">2012 Kovena Arlo 1.8s<br>Sport Touring 4dr Wagon</div>
    <div class="drive">Drive Train :FWD</div>
    <div class="card-meta"><span>⋖ Share</span><span>♡ Like</span><span>▣ 2012</span></div>
  </div>

  <div class="car-card" style="left:758px;top:551px">
    <div class="car-photo" role="img" aria-label="Silver sedan in a dealer lot" style="background:linear-gradient(160deg,#cdd3d9,#a1a7ad 55%,#73787d)"></div>
    <div class="call-bar"><svg width="15" height="15" viewBox="0 0 24 24" fill="currentColor"><path d="M6.6 10.8a15.1 15.1 0 0 0 6.6 6.6l2.2-2.2a1 1 0 0 1 1-.3c1.1.4 2.3.6 3.6.6a1 1 0 0 1 1 1V20a1 1 0 0 1-1 1A17 17 0 0 1 3 4a1 1 0 0 1 1-1h3.5a1 1 0 0 1 1 1c0 1.3.2 2.5.6 3.6a1 1 0 0 1-.3 1z"/></svg>Call Us: 555 010 2545</div>
    <div class="price">$14 490</div>
    <div class="car-name">2012 Kovena Lumen 2.4v<br>Select 4dr Sedan Lumen</div>
    <div class="drive">Drive Train :FWD</div>
    <div class="card-meta"><span>⋖ Share</span><span>♡ Like</span><span>▣ 2012</span></div>
  </div>

  <div class="btn" style="left:513px;top:1000px;width:174px;height:46px">VIEW ALL CARS</div>
</section>

<div class="side-tab" style="top:953px;background:var(--orange)"><i><svg width="13" height="13" viewBox="0 0 24 24" fill="#ff6612"><path d="M6.6 10.8a15.1 15.1 0 0 0 6.6 6.6l2.2-2.2a1 1 0 0 1 1-.3c1.1.4 2.3.6 3.6.6a1 1 0 0 1 1 1V20a1 1 0 0 1-1 1A17 17 0 0 1 3 4a1 1 0 0 1 1-1h3.5a1 1 0 0 1 1 1c0 1.3.2 2.5.6 3.6a1 1 0 0 1-.3 1z"/></svg></i></div>
<div class="side-tab" style="top:1011px;background:var(--blue)"><i><svg width="13" height="13" viewBox="0 0 24 24" fill="#1a62b8"><path d="M2 5h20v14H2z M2 5l10 8 10-8" stroke="#fff" stroke-width="1.5"/></svg></i></div>

<section class="reviews">
  <h2>CLIENT REVIEWS</h2>
  <svg class="abs" style="left:82px;top:213px" width="38" height="74" viewBox="0 0 38 74" fill="none" stroke="#fff" stroke-width="1.5"><path d="M36 2L2 37l34 35"/></svg>
  <svg class="abs" style="left:1083px;top:213px" width="38" height="74" viewBox="0 0 38 74" fill="none" stroke="#fff" stroke-width="1.5"><path d="M2 2l34 35L2 72"/></svg>
  <div class="avatar" style="left:172px;top:186px" role="img" aria-label="Customer portrait"></div>
  <div class="review" style="left:312px;top:175px">
    <div class="stars">★★★★★</div>
    <p>Sed ut perspiciatis unde omnis iste natus error sit voluptatem accusantiumdoloreue laudantium, totam remaperiam, eaque sa quae ab illSed ut perspiciatis und.</p>
    <div class="who">Dale - Marston</div>
  </div>
  <div class="avatar" style="left:626px;top:186px" role="img" aria-label="Customer portrait"></div>
  <div class="review" style="left:765px;top:175px">
    <div class="stars">★★★★★</div>
    <p>Sed ut perspiciatis unde omnis iste natus error sit voluptatem accusantiumdoloreue laudantium, totam remaperiam, eaque sa quae ab illSed ut perspiciatis und.</p>
    <div class="who">Dale - Marston</div>
  </div>
</section>

<div class="finance-media" role="img" aria-label="Video or photo about vehicle financing"></div>
<h2 class="finance-title">FINANCIAL <span>LOAN</span></h2>
<p class="finance-text">Lorem ipsum dolor sit amet, consectetur adipiscing elit, sed do eiusmod tempor incididunt ut labore et dolore magna aliqua. Ut enim ad minim veniam, quis nostrud exercitation ullamco laboris nisi ut aliquip ex ea commodo consequat. Duis aute irure dolor in reprehenderit in voluptate velit esse cillum dolore eu fugiat nulla pariatur. Excepteur sint occaecat cupidatat non proident, sunt in culpa qui officia deserunt molorem ipsum dolor sit amet, consectetur adipiscing elit, sed do eiusmod tempor incididunt ut labore et dolore magna aliqua</p>
<div class="btn" style="left:656px;top:2575px;width:182px;height:46px;font-size:13px">APPLY FOR A LOAN</div>

<section class="promo">
  <svg class="abs" style="left:170px;top:52px" width="58" height="44" viewBox="0 0 58 44" fill="#fff"><path d="M10 4h38l6 14h2a2 2 0 0 1 2 2v14h-6v6a2 2 0 0 1-2 2h-6a2 2 0 0 1-2-2v-6H16v6a2 2 0 0 1-2 2H8a2 2 0 0 1-2-2v-6H0V20a2 2 0 0 1 2-2h2zM13 10l-4 9h40l-4-9z"/><circle cx="11" cy="26" r="4" fill="#ff6612"/><circle cx="47" cy="26" r="4" fill="#ff6612"/></svg>
  <p><i>Shop</i> our best <i>used vehicles</i> to find great deals<br>on the most popular cars for sale near you.</p>
  <div class="btn-dark">SHOP USED CARS</div>
</section>

<section class="tiles">
  <div class="tile" style="left:172px;background:linear-gradient(160deg,#dfe2e5,#a8adb2 60%,#5b5f63)" role="img" aria-label="Silver sedan parked outside the dealership"><span>ARE YOU LOOKING FOR A CAR?</span></div>
  <div class="tile" style="left:612px;background:linear-gradient(160deg,#b4b9bd,#6f6a62 60%,#3b3833)" role="img" aria-label="Bronze crossover in a dealer lot"><span>DO YOU WANT TO SELL A CAR?</span></div>
</section>

<h2 class="section-title clients-title" style="top:3383px">OUR <span>CLIENTS</span></h2>
<div class="client" style="left:172px;top:3468px"><i></i>VELMAR</div>
<div class="client" style="left:347px;top:3468px"><i></i>ORVO</div>
<div class="client" style="left:521px;top:3468px"><i></i>KTZ</div>
<div class="client" style="left:694px;top:3468px"><i></i>PELLAM</div>
<div class="client" style="left:868px;top:3468px"><i></i>MONTRAVEL</div>
<div class="client" style="left:172px;top:3577px"><i></i>DARNSHIRE</div>
<div class="client" style="left:347px;top:3577px"><i></i>WEXMOORE</div>
<div class="client" style="left:521px;top:3577px"><i></i>BRANT</div>
<div class="client" style="left:694px;top:3577px"><i></i>KLAY</div>
<div class="client" style="left:868px;top:3577px"><i></i>ZERTA</div>
<div class="dots"><b></b><b></b><b></b><b class="on"></b><b></b></div>

<h2 class="section-title" style="top:3832px;font-size:32px">POPULAR <span>SEARCHES</span></h2>
<svg class="abs" style="left:82px;top:3992px" width="38" height="74" viewBox="0 0 38 74" fill="none" stroke="#444" stroke-width="1.5"><path d="M36 2L2 37l34 35"/></svg>
<svg class="abs" style="left:1083px;top:3992px" width="38" height="74" viewBox="0 0 38 74" fill="none" stroke="#444" stroke-width="1.5"><path d="M2 2l34 35L2 72"/></svg>
<div class="pop" style="left:172px;background:linear-gradient(160deg,#d5d8db,#8f9397 60%,#4f5256)" role="img" aria-label="White hatchback"><span>4DR SEDAN KLAY</span></div>
<div class="pop" style="left:389px;background:linear-gradient(160deg,#c9cdd1,#7c8085 60%,#3f4245)" role="img" aria-label="Silver sedan"><span>4DR SEDAN KLAY</span></div>
<div class="pop" style="left:606px;background:linear-gradient(160deg,#d3d6d9,#959a9f 60%,#55595d)" role="img" aria-label="White wagon in a lot"><span>4DR SEDAN KLAY</span></div>
<div class="pop" style="left:824px;background:linear-gradient(160deg,#b8bbbd,#6b665e 60%,#35322d)" role="img" aria-label="Bronze crossover"><span>4DR SEDAN KLAY</span></div>

<footer class="site-footer">
  <svg class="abs" style="left:0;top:0" width="1200" height="466" viewBox="0 0 1200 466" preserveAspectRatio="none"><path d="M0 40C300 -8 900 -8 1200 40V466H0z" fill="#1e1e1e"/></svg>
  <div class="pay" style="left:172px;background:#e9e9e9"></div>
  <div class="pay" style="left:206px;background:#e9e9e9"></div>
  <div class="pay" style="left:240px;background:#e9e9e9"></div>
  <div class="pay" style="left:274px;background:#e9e9e9"></div>
  <div class="foot-brand"><span class="b1">Roadline</span><span class="b2">MOTOR DEPOT</span></div>
  <div class="social">Social Network <i></i></div>

  <div class="contact-col" style="left:160px">
    <svg style="margin:0 auto" width="18" height="18" viewBox="0 0 24 24" fill="#fff"><path d="M6.6 10.8a15.1 15.1 0 0 0 6.6 6.6l2.2-2.2a1 1 0 0 1 1-.3c1.1.4 2.3.6 3.6.6a1 1 0 0 1 1 1V20a1 1 0 0 1-1 1A17 17 0 0 1 3 4a1 1 0 0 1 1-1h3.5a1 1 0 0 1 1 1c0 1.3.2 2.5.6 3.6a1 1 0 0 1-.3 1z"/></svg>
    <h3>CALL US</h3>
    <p>Phone:555-014-2277<br>After hours 555-019-9538</p>
  </div>
  <div class="col-divider" style="left:444px"></div>
  <div class="contact-col" style="left:454px">
    <svg style="margin:0 auto" width="18" height="18" viewBox="0 0 24 24" fill="#fff"><path d="M12 3l10 9h-3v9h-5v-6h-4v6H5v-9H2z"/></svg>
    <h3>FIND US</h3>
    <p>48 Harbor Line Rd.<br>Northfield, MI 49000<br><a>Click Here Map</a></p>
  </div>
  <div class="col-divider" style="left:740px"></div>
  <div class="contact-col" style="left:752px">
    <svg style="margin:0 auto" width="20" height="18" viewBox="0 0 24 20" fill="#fff"><path d="M1 2h22v16H1z"/><path d="M1 2l11 9 11-9" fill="none" stroke="#1e1e1e" stroke-width="2"/></svg>
    <h3>EMAIL</h3>
    <p>sales@roadlinedepot.example</p>
  </div>

  <div class="copy">© 2019 Roadline Motor Depot . All Rights Reserved.</div>
  <div class="foot-links"><span>About</span><span>Legal infomation</span><span>Term of service</span><span>Privacy policy</span></div>
  <div class="mini">C4</div>
</footer>

</body>
</html>
```